Quillon Energy Business Cards

I would like to design some options for about 10 sets of double sided business cards for our team with a raised logo with a Silver glossy finished logo. We are a privately funded upstream Oil & Gas producer drilling vertical wells in Central Oklahoma with a long term production (ROI driven) strategy that we implement through an annual drilling program. We are focused on a shallow / vertical / long life / low decline strategy. We are based in downtown Tulsa Oklahoma. I have attached a sample business card and a picture of our hallway logo which we would like to replicate on the business cards.

Target Market(s)

BRQ Accredited Investors and other Oil & Gas Operators

Industry/Entity Type

Upstream Oil & Gas

Contact Information for Business Card

You can see the sample photo attached, but email / website / address / direct phone / Cell Phone / Name / Title / Fax

Font styles to use
Other font styles liked:
• Felix Titling

Colors
0054AA
0677BA
7BADD7
CADEEF
E8F1F8

Requirements
Must have
• Glossy raised logo
Nice to have
• Possibly a new logo.
Should not have
• No Greens /

```html
<!DOCTYPE html>
<html lang="en">
<head>
<meta charset="utf-8">
<title>Quillon Energy Business Cards</title>
<link href="https://fonts.googleapis.com/css2?family=Cinzel:wght@500&family=Montserrat:wght@400;600&display=swap" rel="stylesheet">
<style>
  :root {
    --backdrop: #3b3b3b;
    --card: #121212;
    --silver: #d6d6d6;
    --silver-soft: #a9a9a9;
    --rule: #8a8a8a;
  }
  * { box-sizing: border-box; margin: 0; padding: 0; }
  html, body { width: 1200px; height: 801px; overflow: hidden; }
  body {
    background: var(--backdrop);
    display: flex;
    align-items: center;
    justify-content: center;
    gap: 48px;
    font-family: "Montserrat", sans-serif;
  }
  .card {
    width: 525px;
    height: 300px;
    background: var(--card);
    position: relative;
  }
  .contact-card {
    display: flex;
    align-items: center;
    justify-content: center;
    padding: 0 28px;
  }
  .identity {
    text-align: right;
    padding-right: 14px;
  }
  .identity .person-name {
    font-weight: 600;
    font-size: 15px;
    letter-spacing: 0.04em;
    color: var(--silver);
    text-transform: uppercase;
  }
  .identity .role,
  .identity .department {
    font-size: 11.5px;
    color: var(--silver-soft);
    margin-top: 4px;
  }
  .divider {
    width: 1px;
    height: 112px;
    background: var(--rule);
  }
  .details {
    padding-left: 10px;
    font-size: 11px;
    color: var(--silver-soft);
    line-height: 1.55;
  }
  .details .address { margin-bottom: 4px; }
  .details li {
    list-style: none;
    display: flex;
    align-items: center;
    gap: 6px;
  }
  .details svg { width: 9px; height: 9px; flex: none; }
  .brand-card {
    display: flex;
    align-items: center;
    justify-content: center;
  }
  .brand-name {
    font-family: "Cinzel", serif;
    font-weight: 500;
    font-size: 30px;
    letter-spacing: 0.02em;
    color: var(--silver);
  }
</style>
</head>
<body>
  <section class="card contact-card">
    <div class="identity">
      <p class="person-name">Darian T. Vossberg, CPL</p>
      <p class="role">Executive Vice President</p>
      <p class="department">Land, Legal &amp; Business Development</p>
    </div>
    <div class="divider"></div>
    <div class="details">
      <p class="address">420 South Main Street<br>Suite 900, Tulsa, OK 74103</p>
      <ul>
        <li><svg viewBox="0 0 10 10"><path d="M2 1h2l1 2-1 1a6 6 0 0 0 2 2l1-1 2 1v2c0 1-1 1-1 1A8 8 0 0 1 1 2s0-1 1-1z" fill="#bbb"/></svg>539-555-0142</li>
        <li><svg viewBox="0 0 10 10"><rect x="2.5" y="0.5" width="5" height="9" rx="1" fill="none" stroke="#bbb"/></svg>918-555-0187</li>
        <li><svg viewBox="0 0 10 10"><rect x="1" y="4" width="8" height="5" fill="#bbb"/><rect x="3" y="1" width="4" height="3" fill="none" stroke="#bbb"/></svg>918-555-0163</li>
        <li><svg viewBox="0 0 10 10"><rect x="0.5" y="2" width="9" height="6" fill="none" stroke="#bbb"/><path d="M1 2.5l4 3 4-3" fill="none" stroke="#bbb"/></svg>DTV@QETulsa.com</li>
        <li><svg viewBox="0 0 10 10"><circle cx="5" cy="5" r="4.2" fill="none" stroke="#bbb"/><path d="M1 5h8M5 1c-2 2-2 6 0 8M5 1c2 2 2 6 0 8" fill="none" stroke="#bbb" stroke-width="0.7"/></svg>www.QuillonEnergyLLC.com</li>
      </ul>
    </div>
  </section>

  <section class="card brand-card">
    <p class="brand-name">Quillon Energy, LLC</p>
  </section>
</body>
</html>
```